"Lantern Field" Play - Poster Design for Theatre Group

We are an amateur theatre group based in Geneva, Switzerland. We take pride in eye-catching posters for our shows, which are printed in various sizes.
This design will be for a play in March 2016. The play is called "Lantern Field", and it's a Harwick Medal winner from Marcus Ellery-Pound. The play is about a couple who have everything a family could want, until they lose a child in a life-shattering accident that turns their world upside down. The play charts the couple's bittersweet search to find each other and to find comfort.
Most importantly, we want a design that will make people want to see the show. We don't want to give away the plot or be too heavy-handed about death, but we want it to be clear that it's not a comedy (although there are some lighter moments!).
Attached you will find a template for the poster. This simply has our group name and logo in the top right corner: (Lakeshore Stage Players Circle presents).
You may change the color of both the text and the logo, but please do not change the font, size, or location.
Here is the information that needs to be on the poster, wherever you see fit:
play title: Lantern Field
author byline: by Marcus Ellery-Pound
director line: directed by Rob Feltwick
tagline: How do you keep it together when your whole world's fallen apart?
dates and times:
1-5 March 2016
(Tue-Fri 20:00, Sat 19:00)
location:
Théâtre du Vieux-Moulin
Eaux-Vives, Geneva
websites:
www.lspc.ch
www.scenelettres.ch
Technical Details:
Any font or combination of fonts is acceptable. The largest text should be the play title. The author's name must be at least 50% of the title font size.
For this competition, we would like the version with A3 proportions, which will also be used at F4 (89.5 x 128 cm) and A5 sizes (14.8 x 21 cm). Therefore no text should be below 9pt at A5.
However, from the winning designer we will also need repurposed sizes of the same design. Here is a comprehensive list of the sizes we will need.
1) A3 print poster. Artwork should be 300dpi, CMYK, sent with a 1mm bleed all round, to specification PDF/X-1A:2001. We will need this image in PDF format in addition to the default Artbrigade formats.
2) Chatterly advert picture. 1200px by 628px, RGB jpeg. This must comply with Chatterly’s restrictions on amount of text, which is no more than 20% of area taken up by text.(https://www.chatterly.example/ads/tools/text_overlay).
Because of these restrictions it is sufficient to include just the title and the author's name in this version.
3) Chatterly cover picture: 851px by 314px. RGB jpeg. It is sufficient to include just the title and the author's name in this version.
4) Web banner. 1000px by 300px. RGB jpeg. This version should include just the main image(s), no text.
Theatergoers
Entertainment

```html
<!DOCTYPE html>
<html lang="en">
<head>
<meta charset="utf-8">
<title>Lantern Field — Lakeshore Stage Players Circle</title>
<link rel="stylesheet" href="https://fonts.googleapis.com/css2?family=Anton&family=Arimo&display=swap">
<style>
  :root {
    --ink-dark: #141414;
    --stone-warm: #6b6650;
    --stone-warm-deep: #2a271c;
    --stone-cool: #6d6f73;
    --stone-cool-deep: #1c1d20;
    --light-core: #ffffff;
    --text-white: #ffffff;
    --text-grey: #d9d9d9;
    --director-label: #1a1a1a;
    --director-red: #c4262e;
  }
  * { margin: 0; padding: 0; box-sizing: border-box; }
  html, body { width: 865px; height: 1200px; overflow: hidden; background: var(--ink-dark); }
  .poster {
    position: relative; width: 865px; height: 1200px; overflow: hidden;
    font-family: "Anton", "Arial Narrow", sans-serif; color: var(--text-white);
  }
  .stairwell-photo {
    position: absolute; inset: 0;
    background:
      radial-gradient(circle at 460px 690px, var(--light-core) 0 75px, rgba(230,230,230,.85) 100px, rgba(150,150,150,.35) 190px, transparent 320px),
      linear-gradient(90deg, var(--stone-warm-deep) 0%, var(--stone-warm) 22%, rgba(110,105,80,.9) 48.5%, var(--stone-cool) 48.5%, #505256 75%, var(--stone-cool-deep) 100%);
  }
  .stairwell-photo::after {
    content: ""; position: absolute; inset: 0;
    background: linear-gradient(180deg, rgba(10,10,10,.55) 0%, transparent 30%, transparent 62%, rgba(10,10,10,.8) 100%);
  }
  .presenter {
    position: absolute; top: 40px; right: 44px;
    display: flex; align-items: center; gap: 12px;
  }
  .presenter-name {
    font-size: 17px; line-height: 22px; text-align: right; color: var(--text-grey);
    width: 150px;
  }
  .presenter-mark {
    width: 100px; height: 100px; border-radius: 50%;
    border: 3px solid var(--text-grey);
  }
  .title-art { position: absolute; inset: 0; }
  .play-title { font-size: 92px; fill: var(--text-white); }
  .play-author { font-size: 46px; fill: var(--text-white); }
  .tagline {
    position: absolute; top: 985px; left: 0; width: 865px; text-align: center;
    font-size: 24px; line-height: 31px;
  }
  .director-label { font-size: 11px; color: var(--director-label); margin-left: 6px; }
  .director-name { font-size: 25px; color: var(--director-red); margin-left: 4px; }
  .show-details {
    position: absolute; top: 1060px; left: 0; width: 865px; text-align: center;
    font-family: "Arimo", Arial, sans-serif; font-size: 20px; line-height: 29px;
  }
</style>
</head>
<body>
<main class="poster">
  <div class="stairwell-photo" role="img" aria-label="Photograph looking up a spiral stone stairwell toward a bright window with a dark cross frame"></div>

  <div class="presenter">
    <p class="presenter-name">Lakeshore Stage Players Circle presents</p>
    <span class="presenter-mark"></span>
  </div>

  <svg class="title-art" width="865" height="1200" viewBox="0 0 865 1200">
    <defs>
      <path id="title-arc" d="M100 345 Q 330 110 610 370"/>
      <path id="author-arc" d="M612 385 Q 650 650 565 915"/>
    </defs>
    <text class="play-title"><textPath href="#title-arc" textLength="560" lengthAdjust="spacingAndGlyphs">Lantern Field</textPath></text>
    <text class="play-author"><textPath href="#author-arc" textLength="520" lengthAdjust="spacingAndGlyphs">by Marcus Ellery-Pound</textPath></text>
  </svg>

  <p class="tagline">How do you keep it together when your whole world's<br>fallen apart?<span class="director-label">directed by</span><span class="director-name">Rob Feltwick</span></p>

  <p class="show-details">1-5 March 2016 (Tue-Fri 20:00, Sat 19:00)<br>Théâtre du Vieux-Moulin, Eaux-Vives, Geneva www.lspc.ch<br>www.scenelettres.ch</p>
</main>
</body>
</html>
```